Business Card for Property Management Firm
Halvorsen Crest Property Management
Creative Brief
Professional
Dean Olwright
Broker
7182 Marbury Lane Los Alamitos Ca 90731
dean@hcpmxv.com
www.HCPropertymanagement.example
Please include the following items to be highlighted on the other folds of the business cards if they fit 1.) Top 1% of Leasing Brokerages in Southern California 2.) Ranked Top 5 Leasing Agents in Orange County 3 Years Running 3.) "Proudly Managing Over 100 Million in Real Estate Assets" 4.) If room permits you can also add: HCPM - Residential Property Management Solutions
see comments above

```html
<!DOCTYPE html>
<html lang="en">
<head>
<meta charset="utf-8">
<title>Halvorsen Crest Property Management – Business Card</title>
<link rel="stylesheet" href="https://fonts.googleapis.com/css2?family=Open+Sans:wght@400;600;700&display=swap">
<style>
  :root {
    --backdrop: #e3e4e4;
    --card: #ffffff;
    --teal: #4f7d79;
    --charcoal: #393a3c;
    --ink: #2f3032;
    --on-dark: #ffffff;
  }
  * { margin: 0; padding: 0; box-sizing: border-box; }
  html, body {
    width: 1200px;
    height: 883px;
    overflow: hidden;
    background: var(--backdrop);
    font-family: "Open Sans", Arial, sans-serif;
  }
  .card {
    position: absolute;
    left: 330px;
    width: 540px;
    height: 310px;
    background: var(--card);
    border-radius: 20px;
    overflow: hidden;
    box-shadow: 0 2px 6px rgba(0,0,0,0.12);
  }
  .card--front { top: 70px; }
  .card--back { top: 503px; }

  /* Front */
  .brand {
    position: absolute;
    left: 48px;
    top: 126px;
    display: flex;
    align-items: center;
    gap: 12px;
  }
  .brand__square {
    width: 40px;
    height: 40px;
    background: var(--charcoal);
  }
  .brand__name {
    color: var(--charcoal);
    font-weight: 600;
    font-size: 15px;
    line-height: 1.2;
    letter-spacing: 0.06em;
    text-transform: uppercase;
  }
  .brand__name span { display: block; font-size: 9.5px; letter-spacing: 0.14em; }
  .front-band {
    position: absolute;
    right: 0;
    top: 80px;
    width: 250px;
    height: 52px;
    background: var(--charcoal);
  }
  .front-band__web {
    position: absolute;
    left: 0;
    top: 0;
    width: 200px;
    height: 100%;
    background: var(--teal);
    color: var(--on-dark);
    font-size: 9px;
    letter-spacing: 0.04em;
    text-transform: uppercase;
    display: flex;
    align-items: center;
    justify-content: center;
  }

  /* Back */
  .person {
    position: absolute;
    right: 120px;
    top: 42px;
    text-align: right;
    color: var(--ink);
  }
  .person__name {
    font-size: 22px;
    font-weight: 400;
    letter-spacing: 0.03em;
    text-transform: uppercase;
  }
  .person__name strong { font-weight: 700; }
  .person__title {
    font-size: 10px;
    font-weight: 700;
    letter-spacing: 0.06em;
    text-transform: uppercase;
    color: var(--teal);
  }
  .contact-phone {
    position: absolute;
    left: 0;
    top: 140px;
    width: 262px;
    height: 82px;
    background: var(--teal);
    color: var(--on-dark);
    text-align: right;
    padding: 20px 18px 0 0;
    font-size: 11px;
    line-height: 1.35;
    text-transform: uppercase;
    letter-spacing: 0.04em;
  }
  .contact-web {
    position: absolute;
    left: 262px;
    right: 0;
    top: 108px;
    height: 84px;
    background: var(--charcoal);
    color: var(--on-dark);
    padding: 18px 0 0 18px;
    font-size: 11px;
    line-height: 1.35;
    letter-spacing: 0.03em;
  }
  .contact__label { font-weight: 600; text-transform: uppercase; }
  .contact-web .contact__item { text-transform: uppercase; font-size: 10px; }
  .contact-web .contact__item--mail { text-transform: none; }
  .address {
    position: absolute;
    left: 280px;
    top: 206px;
    color: var(--ink);
    font-size: 9.5px;
    font-weight: 600;
    line-height: 1.4;
    letter-spacing: 0.04em;
    text-transform: uppercase;
  }
</style>
</head>
<body>
  <section class="card card--front" aria-label="Business card front">
    <div class="brand">
      <div class="brand__square"></div>
      <div class="brand__name">Halvorsen Crest<span>Property Management</span></div>
    </div>
    <div class="front-band">
      <div class="front-band__web">www.HCPropertymanagement.example</div>
    </div>
  </section>

  <section class="card card--back" aria-label="Business card back">
    <div class="person">
      <div class="person__name">Dean <strong>Olwright</strong></div>
      <div class="person__title">Broker</div>
    </div>
    <div class="contact-web">
      <div class="contact__label">Email &amp; Web</div>
      <div class="contact__item contact__item--mail">dean@hcpmxv.com</div>
      <div class="contact__item">www.HCPropertymanagement.example</div>
    </div>
    <div class="contact-phone">
      <div class="contact__label">Phone &amp; Fax</div>
      <div class="contact__item">+1 562 555 0147</div>
      <div class="contact__item">+1 562 555 0182</div>
    </div>
    <div class="address">7182 Marbury Lane Los Alamitos<br>Ca 90731</div>
  </section>
</body>
</html>
```